Commercial painting company is looking for a creative website designer.

Hi, we just completed our logo project and now ready to launch our website. The project will be done on Squarespace platform. It will contain:
Page 1 HOME
Page 2 SERVICES
Page 3 PICTURES
The content will be written by us. I am not sure bout the pictures, I do not have any to provide. I can buy stock photos if needed.
We are commercial only painting company and have to appeal to commercial, industrial property mangers. We will need CALL, REQUEST FOR ESTIMATE buttons.
If possible to have a live picture on home page would be great. Thank you
Target Market(s)
Property Managers
Industry/Entity Type
Commercial Painting
Other font styles liked:
- Poppins

```html
<!DOCTYPE html>
<html lang="en">
<head>
<meta charset="utf-8">
<title>Brightcoat Commercial – Home</title>
<link href="https://fonts.googleapis.com/css2?family=Poppins:wght@400;500;600;700&display=swap" rel="stylesheet">
<style>
:root{
  --navy:#072a6e;
  --navy-deep:#051f55;
  --red:#c8203f;
  --ink:#111827;
  --grey-text:#5b6270;
  --field:#dcdcdc;
  --backdrop:#dedede;
  --white:#ffffff;
}
*{margin:0;padding:0;box-sizing:border-box}
html,body{width:667px;height:1200px;overflow:hidden;background:var(--backdrop);font-family:'Poppins',sans-serif}
.stage{position:absolute;left:0;top:0;width:1431px;height:2576px;transform:scale(0.4661);transform-origin:0 0}
.page{position:absolute;left:320px;top:117px;width:790px;height:2248px;background:var(--white);box-shadow:0 10px 40px rgba(0,0,0,.18);overflow:hidden}
.abs{position:absolute}
.btn{position:absolute;background:var(--red);color:var(--white);font-weight:600;font-size:10px;display:flex;align-items:center;justify-content:center;border-radius:3px;box-shadow:0 3px 6px rgba(200,32,63,.35)}

.topbar{left:0;top:0;width:790px;height:41px;background:var(--navy)}
.topbar .item{position:absolute;top:0;height:41px;display:flex;align-items:center;gap:7px;color:var(--white);font-size:10px;font-weight:600}
.topbar .divider{position:absolute;left:443px;top:14px;height:16px;border-left:1px dotted rgba(255,255,255,.5)}
.estimate-tab{position:absolute;left:590px;top:0;width:200px;height:41px;background:var(--red);color:var(--white);font-size:10px;font-weight:600;display:flex;align-items:center;justify-content:center;gap:7px}
.navbar{left:0;top:41px;width:790px;height:59px;background:var(--white)}
.navbar a{position:absolute;top:21px;font-size:11px;color:#333;text-decoration:none}
.brand{position:absolute;left:50px;top:9px;width:88px;height:88px;border-radius:50%;background:var(--white);border:3px solid var(--navy);display:flex;align-items:center;justify-content:center;text-align:center;font-size:11px;font-weight:700;color:var(--navy);line-height:1.2;z-index:3}

.hero{left:0;top:100px;width:790px;height:409px;background:linear-gradient(90deg,#5f7fa0 0%,#7d97b3 45%,#6f8ea8 62%,#9fbea0 80%,#b9cfb6 100%)}
.hero-panel{left:0;top:195px;width:425px;height:187px;background:rgba(232,238,244,.8)}
.hero-title{left:50px;top:218px;font-size:27px;font-weight:700;color:#1c2a4e;white-space:nowrap}
.hero-title span{color:var(--red)}
.hero-text{left:49px;top:258px;width:360px;font-size:14px;line-height:25px;color:#5a6272}

.welcome{left:0;top:563px;width:790px;text-align:center}
.welcome .kicker{font-size:17px;font-weight:700;color:var(--ink)}
.welcome .name{font-size:21px;font-weight:700;color:var(--red);margin-top:2px}
.about-photo{left:52px;top:649px;width:285px;height:250px;background:linear-gradient(180deg,#a9bdd2 0%,#d8dde2 45%,#b8b8b4 60%,#4c5259 100%)}
.about-heading{left:397px;top:645px;width:350px;font-size:18px;font-weight:600;line-height:24px;color:var(--ink)}
.about-text{left:397px;top:720px;width:355px;font-size:10px;line-height:20px;color:#444}
.about-text p+p{margin-top:19px}

.services{left:0;top:959px;width:790px;height:541px;background:radial-gradient(ellipse at 50% 80%,#1d3f86 0%,var(--navy) 70%)}
.services-sub{left:0;top:1068px;width:790px;text-align:center;color:var(--white);font-size:10px}
.card{position:absolute;top:1113px;width:206px;height:303px;background:var(--white);border-radius:3px;text-align:center;box-shadow:0 6px 18px rgba(0,0,0,.3)}
.card .photo{width:206px;height:148px;border-radius:3px 3px 0 0}
.card .icon{position:absolute;left:83px;top:128px;width:40px;height:40px;border-radius:50%;background:var(--white);border:1.5px solid var(--red);display:flex;align-items:center;justify-content:center}
.card h3{margin-top:30px;font-size:12px;font-weight:600;color:var(--ink)}
.card p{margin:11px auto 0;width:150px;font-size:9px;line-height:14px;color:#555}
.card .more{display:inline-block;margin-top:12px;font-size:9.5px;color:var(--red);text-decoration:underline}

.estimate-title{left:0;top:1543px;width:790px;text-align:center;font-size:17px;font-weight:700;color:var(--ink)}
.estimate-rule{left:359px;top:1579px;width:40px;height:3px;background:var(--red)}
.estimate-sub{left:0;top:1597px;width:790px;text-align:center;font-size:10px;color:#444}
.field{position:absolute;background:var(--field);border-radius:2px;font-size:10px;color:#666;padding:14px 0 0 24px}

.footer{left:0;top:1986px;width:790px;height:262px;background:var(--navy)}
.copyright{left:0;top:2225px;width:790px;height:23px;background:var(--navy-deep);color:#aab5cc;font-size:9px;display:flex;align-items:center;justify-content:center}
.foot-brand{left:49px;top:2031px;width:44px;height:44px;border-radius:50%;background:var(--white);color:var(--navy);font-size:6px;font-weight:700;display:flex;align-items:center;justify-content:center;text-align:center;line-height:1.1}
.foot-about{left:50px;top:2082px;width:200px;font-size:11px;line-height:20px;color:#aab7d3}
.social{position:absolute;top:2131px;width:24px;height:24px;border-radius:50%;background:#8d9cbf}
.col-title{position:absolute;top:2033px;font-size:11px;font-weight:600;color:var(--white)}
.col-title::after{content:"";display:block;width:16px;height:2px;background:var(--white);margin-top:6px}
.col-link{position:absolute;font-size:11px;color:#aab7d3;display:flex;align-items:center;gap:8px;white-space:nowrap}
</style>
</head>
<body>
<div class="stage">
<div class="page">

  <div class="abs topbar">
    <div class="item" style="left:352px">
      <svg width="14" height="14" viewBox="0 0 24 24" fill="none" stroke="#fff" stroke-width="2"><path d="M12 22s7-7 7-12a7 7 0 0 0-14 0c0 5 7 12 7 12z"/><circle cx="12" cy="10" r="2.5"/></svg>
      Westbrook
    </div>
    <div class="divider"></div>
    <div class="item" style="left:470px">
      <svg width="15" height="15" viewBox="0 0 24 24" fill="none" stroke="#fff" stroke-width="2"><path d="M5 3h4l2 5-3 2a12 12 0 0 0 6 6l2-3 5 2v4a2 2 0 0 1-2 2A17 17 0 0 1 3 5a2 2 0 0 1 2-2z"/></svg>
      555 - 0142 870
    </div>
    <div class="estimate-tab">
      <svg width="13" height="14" viewBox="0 0 24 24" fill="none" stroke="#fff" stroke-width="2"><rect x="5" y="4" width="14" height="18" rx="2"/><path d="M9 2h6v4H9zM12 10v6M9 13h6"/></svg>
      GET FREE ESTIMATE
    </div>
  </div>

  <div class="brand">Brightcoat<br>Commercial</div>

  <nav class="abs navbar">
    <a style="left:271px">Home</a>
    <a style="left:362px">Services&nbsp;⌄</a>
    <a style="left:467px">Pictures</a>
    <a style="left:570px">About Us</a>
    <a style="left:678px">Contact Us</a>
  </nav>

  <div class="abs hero" role="img" aria-label="Painters on ropes painting the facade of a multi-storey building"></div>
  <div class="abs hero-panel"></div>
  <h1 class="abs hero-title">BRIGHTCOAT <span>COMMERCIAL</span></h1>
  <p class="abs hero-text">Lorem Ipsum is simply dummy text of the printing and typesetting industry.</p>
  <div class="btn" style="left:50px;top:325px;width:120px;height:29px">More About Us</div>

  <div class="abs welcome">
    <div class="kicker">WELCOME TO</div>
    <div class="name">BRIGHTCOAT COMMERCIAL</div>
  </div>
  <div class="abs about-photo" role="img" aria-label="Freshly painted commercial building beside a parking lot under a cloudy sky"></div>
  <h2 class="abs about-heading">Lorem Ipsum is simply dummy text<br>of&nbsp; printing and typesetting industry.</h2>
  <div class="abs about-text">
    <p>Lorem Ipsum is simply dummy text of the printing and typesetting industry. Lorem Ipsum has been the industry's standard dummy text</p>
    <p>when an unknown printer took a galley of type and scrambled it to make a type specimen book. It has survived not only five centuries, but also the leap into electronic typesetting, remaining essentially.</p>
  </div>
  <div class="btn" style="left:397px;top:869px;width:120px;height:29px">More About Us</div>

  <section class="abs services"></section>
  <p class="abs services-sub">Lorem Ipsum is simply dummy text of the printing and typesetting</p>

  <div class="card" style="left:50px">
    <div class="photo" role="img" aria-label="Worker painting an exterior wall beside scaffolding" style="background:linear-gradient(135deg,#e4e6e8,#9aa0a6)"></div>
    <div class="icon"><svg width="20" height="20" viewBox="0 0 24 24" fill="none" stroke="#c8203f" stroke-width="1.6"><path d="M14 3l7 7-6 6-7-7zM8 9l-4 4 2 2-3 5 5-3 2 2 4-4"/></svg></div>
    <h3>Interior Painting</h3>
    <p>Lorem Ipsum is simply dummy text of the printing and typesetting industry.</p>
    <span class="more">Read More</span>
  </div>
  <div class="card" style="left:292px">
    <div class="photo" role="img" aria-label="Painter working in a bright empty interior" style="background:linear-gradient(90deg,#7a5a3e,#e9e7e3 45%,#c8ccd1)"></div>
    <div class="icon"><svg width="20" height="20" viewBox="0 0 24 24" fill="none" stroke="#c8203f" stroke-width="1.6"><rect x="4" y="3" width="14" height="6" rx="1"/><path d="M18 6h2v5h-8v3M10 14h4v7h-4z"/></svg></div>
    <h3>Exterior Painting</h3>
    <p>Lorem Ipsum is simply dummy text of the printing and typesetting industry.</p>
    <span class="more">Read More</span>
  </div>
  <div class="card" style="left:534px">
    <div class="photo" role="img" aria-label="Room with paint cans, a ladder and colour-striped wall" style="background:linear-gradient(90deg,#e8ecef 40%,#f4e59a 60%,#f3a37e 78%,#e8507a 100%)"></div>
    <div class="icon"><svg width="20" height="20" viewBox="0 0 24 24" fill="none" stroke="#c8203f" stroke-width="1.6"><path d="M12 3a9 9 0 0 0 0 18c1.5 0 2-1 1.5-2s0-2 1.5-2h3a3 3 0 0 0 3-3c0-6-4-11-9-11z"/><circle cx="8" cy="11" r="1.3"/><circle cx="11" cy="7" r="1.3"/><circle cx="15.5" cy="8" r="1.3"/></svg></div>
    <h3>Color Consultation</h3>
    <p>Lorem Ipsum is simply dummy text of the printing and typesetting industry.</p>
    <span class="more">Read More</span>
  </div>
  <div class="btn" style="left:335px;top:1449px;width:120px;height:29px">More</div>

  <h2 class="abs estimate-title">REQUEST A FREE ESTIMATE</h2>
  <div class="abs estimate-rule"></div>
  <p class="abs estimate-sub">Lorem Ipsum is simply dummy text of the printing and typesetting</p>
  <div class="field" style="left:118px;top:1655px;width:268px;height:39px">First Name</div>
  <div class="field" style="left:402px;top:1655px;width:268px;height:39px">Last name</div>
  <div class="field" style="left:118px;top:1711px;width:268px;height:39px">Email Address</div>
  <div class="field" style="left:402px;top:1711px;width:268px;height:39px">Phone Number</div>
  <div class="field" style="left:118px;top:1768px;width:552px;height:107px">Message</div>
  <div class="btn" style="left:342px;top:1903px;width:120px;height:29px">SUBMIT NOW</div>

  <footer class="abs footer"></footer>
  <div class="abs foot-brand">Brightcoat</div>
  <p class="abs foot-about">Lorem Ipsum is simply dummy text of the printing and typesetting</p>
  <div class="social" style="left:49px"></div>
  <div class="social" style="left:85px"></div>
  <div class="social" style="left:121px"></div>

  <div class="col-title" style="left:334px">Site Links</div>
  <div class="col-link" style="left:333px;top:2083px;color:#fff">Home</div>
  <div class="col-link" style="left:333px;top:2116px">Privacy</div>
  <div class="col-link" style="left:333px;top:2149px">Help</div>

  <div class="col-title" style="left:467px">Company</div>
  <div class="col-link" style="left:466px;top:2087px">About Us</div>
  <div class="col-link" style="left:466px;top:2119px">Services</div>
  <div class="col-link" style="left:466px;top:2152px">Pictures</div>

  <div class="col-title" style="left:598px">Contact</div>
  <div class="col-link" style="left:598px;top:2087px"><svg width="12" height="12" viewBox="0 0 24 24" fill="none" stroke="#aab7d3" stroke-width="2"><path d="M12 22s7-7 7-12a7 7 0 0 0-14 0c0 5 7 12 7 12z"/><circle cx="12" cy="10" r="2.5"/></svg>#48, Harbor Lane, WB</div>
  <div class="col-link" style="left:598px;top:2119px"><svg width="12" height="12" viewBox="0 0 24 24" fill="none" stroke="#aab7d3" stroke-width="2"><path d="M5 3h4l2 5-3 2a12 12 0 0 0 6 6l2-3 5 2v4a2 2 0 0 1-2 2A17 17 0 0 1 3 5a2 2 0 0 1 2-2z"/></svg>555 - 0142 870</div>
  <div class="col-link" style="left:598px;top:2152px"><svg width="12" height="12" viewBox="0 0 24 24" fill="none" stroke="#aab7d3" stroke-width="2"><rect x="3" y="5" width="18" height="14" rx="2"/><path d="M3 7l9 6 9-6"/></svg>Westbrook</div>

  <div class="abs copyright">Copyright © 2010-2023 Brightcoat Commercial</div>

</div>
</div>
</body>
</html>
```